Computer screen desktop background design for dentists orthodontic office PCs

We need a new design to use as the Windows desktop background picture for the PC workstations in a dentists orthodontic office.
The design should be vector graphics.
The aspect ratio should reflect the monitor size (Resolution: 1920x1200).
In the uploaded files you can find the logo, the fonts and the design of the business card.
The design should not be brighter than the Windows 10 background picture (monitor lifetime).

The office logo must be the dominating part of the design (see uploaded files).

You don't need to use the same fonts, but the used fonts have to be in harmony with the fonts used in the logo and the business card.
The colors used have to be in harmony with the logo.
All the text below must be on the design.
The logical text groups are separated by empty lines.

Kieferorthopädie Tannwiese

Dr. med. dent. Lukas Brenner
Fachzahnarzt für Kieferorthopädie (CH) (Important information!)

Please make something cool and modern that attracts the patient's attraction when seen on the monitor screen.

Target Market(s)

dentists orthodontic office

Industry/Entity Type

Computer

Font styles to use
Sans Serif

Colors

Designer to choose colors to be used in the design.

Requirements
Must have
• The design should be vector graphics.
• The aspect ratio should reflect the monitor size (Resolution: 1920x1200).
• In the uploaded files you can find the logo, the fonts and the design of the business card.
• The design should not be brighter than the Windows 10 background picture (monitor lifetime).
• The office logo must be the dominating part of the design (see uploaded files).
• You don't need to use the same fonts, but the used fonts have to be in harmony with the fonts used in the logo and the business card.
• The colors used have to be in harmony with the logo.
• All the text below must be on the design.
• The logical text groups are separated by empty lines.
• Kieferorthopädie Tannwiese
• Dr. med. dent. Lukas Brenner
• Fachzahnarzt für Kieferorthopädie (CH) (Important information!)
• Adobe Illustrator source files
Nice to have
• Please make something cool and modern that attracts the patient's attraction when seen on the monitor screen.
Should not have

```html
<!DOCTYPE html>
<html lang="de">
<head>
<meta charset="utf-8">
<title>Kieferorthopädie Tannwiese – Desktop</title>
<link rel="stylesheet" href="https://fonts.googleapis.com/css2?family=Roboto:wght@700&family=Saira+Semi+Condensed:wght@400;500&display=swap">
<style>
  :root {
    --page-bg: #e9e6e1;
    --wallpaper-blue: #0b5e9e;
    --wallpaper-blue-deep: #08528c;
    --text-white: #ffffff;
    --text-light-blue: #8fd0f5;
  }
  html, body {
    margin: 0;
    padding: 0;
    width: 1200px;
    height: 1000px;
    overflow: hidden;
    background: var(--page-bg);
  }
  .wallpaper {
    position: absolute;
    left: 0;
    top: 125px;
    width: 1200px;
    height: 750px;
    background: linear-gradient(160deg, var(--wallpaper-blue) 0%, var(--wallpaper-blue) 55%, var(--wallpaper-blue-deep) 100%);
    overflow: hidden;
  }
  .brand {
    position: absolute;
    left: 110px;
    top: 160px;
    display: flex;
    align-items: center;
    gap: 40px;
  }
  .brand-dot {
    width: 150px;
    height: 150px;
    border-radius: 50%;
    background: var(--text-white);
    flex: none;
  }
  .brand-name {
    margin: 0;
    font-family: "Roboto", sans-serif;
    font-weight: 700;
    font-size: 56px;
    letter-spacing: 0.2px;
    color: var(--text-white);
    white-space: nowrap;
  }
  .doctor {
    position: absolute;
    right: 150px;
    top: 440px;
    text-align: right;
    font-family: "Saira Semi Condensed", sans-serif;
  }
  .doctor-name {
    margin: 0;
    font-weight: 500;
    font-size: 56px;
    line-height: 1.1;
    color: var(--text-light-blue);
    white-space: nowrap;
  }
  .doctor-title {
    margin: 14px 0 0;
    font-weight: 400;
    font-size: 35px;
    line-height: 1.1;
    color: var(--text-white);
    white-space: nowrap;
  }
</style>
</head>
<body>
  <main class="wallpaper">
    <div class="brand">
      <span class="brand-dot" aria-hidden="true"></span>
      <h1 class="brand-name">Kieferorthopädie Tannwiese</h1>
    </div>
    <div class="doctor">
      <p class="doctor-name">Dr. med. dent. Lukas Brenner</p>
      <p class="doctor-title">Fachzahnarzt für Kieferorthopädie (CH)</p>
    </div>
  </main>
</body>
</html>
```